Need a Menu with our Logo and price and food items

Need to develop a Menu page that attracts our customers with our logo we have a basic logo and is very poor I can attach our logo and menu Please help us. The Restaurant menu is attached it must be two pages.must include a little of our history which I will provide very soon.

Industry/Entity Type

Restaurant

Font styles to use
Sans Serif

Requirements
Must have
• Casa Benvidal
1837 Calle Orvena
Punta Los Cedrales
San Juan, PR 000912
tel (787) 513-4072
email: casabenvidalpr@fondamail.com
Nice to have
• a google map for directions

```html
<!DOCTYPE html>
<html lang="en">
<head>
<meta charset="utf-8">
<title>Casa Benvidal – Menu</title>
<link rel="stylesheet" href="https://fonts.googleapis.com/css2?family=Great+Vibes&family=Open+Sans:ital,wght@0,400;0,600;0,700;1,400&family=Cormorant+Garamond:ital@1&display=swap">
<style>
  :root{
    --backdrop:#e4e4e2;
    --label:#6f6f6f;
    --wood-1:#6a371b;
    --wood-2:#7b4425;
    --wood-3:#8a5030;
    --card:#f4ece6;
    --card-edge:#e8dcd2;
    --brown:#7a3a1b;
    --tan:#c8997a;
    --welcome:#a9714d;
    --teal:#1d8e98;
    --body:#5a3a2a;
    --note:#7a6a60;
    --contact:#8a3d1c;
    --white:#ffffff;
  }
  *{box-sizing:border-box;margin:0;padding:0}
  html,body{width:1200px;height:496px;overflow:hidden}
  body{background:var(--backdrop);font-family:"Open Sans",sans-serif;position:relative}

  .spread-label{position:absolute;top:30px;font-family:"Cormorant Garamond",serif;font-style:italic;font-size:14px;color:var(--label);transform:translateX(-50%)}

  .spread{position:absolute;top:60px;height:398px;
    background:
      linear-gradient(180deg,rgba(255,255,255,.06),rgba(0,0,0,.12)),
      repeating-linear-gradient(90deg,var(--wood-1) 0 6px,var(--wood-2) 6px 14px,var(--wood-3) 14px 17px,var(--wood-2) 17px 25px,var(--wood-1) 25px 31px);
    box-shadow:0 2px 6px rgba(0,0,0,.35)}
  .spread-outer{left:20px;width:572px}
  .spread-inner{left:612px;width:570px}
  .fold{position:absolute;top:0;bottom:0;width:2px;background:linear-gradient(90deg,rgba(0,0,0,.35),rgba(255,255,255,.12))}

  .card{position:absolute;background:linear-gradient(180deg,var(--white),var(--card) 40%,var(--card-edge));border-radius:8px;box-shadow:0 2px 5px rgba(0,0,0,.4)}

  .script{font-family:"Great Vibes",cursive;font-weight:400}

  /* back cover */
  .back-card{left:18px;top:12px;width:244px;height:372px}
  .back-name{position:absolute;left:8px;top:8px;font-family:"Open Sans",sans-serif;font-weight:600;font-size:15px;color:var(--teal)}
  .back-copy{position:absolute;left:8px;top:34px;width:128px;font-size:6.3px;line-height:8px;color:var(--body)}
  .back-copy p{margin-bottom:6px}
  .contact{position:absolute;left:124px;top:316px;width:116px;background:var(--contact);border-radius:3px;color:var(--white);font-size:5.2px;line-height:7.2px;padding:4px 4px;white-space:nowrap}
  .contact b{font-weight:600;display:inline-block;width:18px}

  /* photos */
  .photo{position:absolute;background:var(--white);padding:4px 4px 12px;box-shadow:0 2px 4px rgba(0,0,0,.4)}
  .shot{width:100%;height:100%}
  .cap{position:absolute;left:0;right:0;bottom:1px;text-align:center;font-family:"Great Vibes",cursive;font-size:7px;color:var(--tan);white-space:nowrap}
  .warm{background:radial-gradient(circle at 55% 45%,#d7a36a,#7b4a2a 55%,#3c2a22)}
  .plate{background:radial-gradient(circle at 50% 50%,#f1ece4 30%,#b9c0a0 42%,#6a7a5a 60%,#3a3a32)}
  .stew{background:radial-gradient(circle at 50% 50%,#6e3b1e 25%,#cfc8bd 45%,#8a8478 70%)}
  .room{background:linear-gradient(180deg,#d9c7a0,#8a5a3a 60%,#4a2a1e)}
  .gallery{background:linear-gradient(160deg,#8a9aa0,#3e5260 55%,#2a2a30)}
  .crowd{background:linear-gradient(180deg,#6a4a7a,#3c2c46 50%,#1e1a26)}
  .mapfill{background:linear-gradient(135deg,#eef0ea,#d8dcd0 60%,#a9c9d8)}
  .shrimp{background:radial-gradient(circle at 50% 50%,#f0b070,#c86a2a 45%,#f2eee8 70%)}

  /* front cover */
  .welcome{position:absolute;left:290px;top:46px;width:276px;text-align:center;font-size:54px;color:var(--welcome);line-height:1}
  .brand{position:absolute;left:286px;top:96px;width:284px;text-align:center;font-family:"Open Sans",sans-serif;font-weight:600;font-size:34px;color:var(--white);letter-spacing:.5px}
  .front-card{left:300px;top:188px;width:246px;height:196px}
  .enjoy{position:absolute;top:8px;left:0;right:0;text-align:center;font-size:37px;color:var(--tan)}
  .sections{position:absolute;top:66px;left:0;right:0;list-style:none;text-align:center;font-size:15.5px;line-height:24.5px;color:var(--brown)}
  .sections li::before,.sections li::after{content:"•";color:var(--tan);margin:0 6px;font-size:12px}

  /* inside pages */
  .page-card{top:12px;height:372px;width:244px}
  .page-left{left:22px}
  .page-right{left:304px;width:246px}
  .heading{position:absolute;right:12px;font-size:24px;color:var(--tan);white-space:nowrap;line-height:1.2}
  .col{position:absolute;display:flex;flex-direction:column}
  .entry{height:20.5px;overflow:hidden}
  .item{display:flex;align-items:baseline;font-size:7px;line-height:9.5px;font-weight:600;color:var(--brown);white-space:nowrap}
  .item .dots{flex:1;border-bottom:1px dotted var(--brown);margin:0 1px;transform:translateY(-2px)}
  .ingr{font-size:4.4px;font-style:italic;color:var(--note);line-height:5.4px;white-space:nowrap;overflow:hidden}
  .drinks .item{height:12px}
</style>
</head>
<body>

<span class="spread-label" style="left:163px">Back Cover</span>
<span class="spread-label" style="left:448px">Front Cover</span>
<span class="spread-label" style="left:737px">Inside Left Page</span>
<span class="spread-label" style="left:1042px">Inside Right Page</span>

<!-- Outer spread -->
<section class="spread spread-outer">
  <div class="fold" style="left:280px"></div>

  <div class="card back-card">
    <h2 class="back-name">Casa Benvidal</h2>
    <div class="back-copy">
      <p>Casa Benvidal is a great place to relax and have a wonderful dinner.</p>
      <p>We serve mediterranean cuisine and tipical Puerto-Rican food, and also fusion of both of them, making some delicious new plates like our risotto with gandules and carne ahumada, smoked with mango and guaba wood, desserts made here in-house, fresh lobster from Puerto Rico and the best osso buco you'll ever have!</p>
      <p>We are a family operated restaurant and our service is very high quality - so come on over and be the judge of it. Also, you will enjoy an artwork exposition by the famous Puerto-Rican painter and artist Rafael Ostiguín.</p>
    </div>
    <div class="contact">
      1837 Calle Orvena, Punta Los Cedrales<br>
      San Juan, PR 00912<br>
      <b>Hours</b>Thursday to Sunday, 11am - 11pm<br>
      <b>Phone</b>(787) 513-4072<br>
      <b>E-mail</b>casabenvidalpr@fondamail.com
    </div>
  </div>

  <figure class="photo" style="left:158px;top:8px;width:96px;height:92px;transform:rotate(4deg)">
    <div class="shot gallery" role="img" aria-label="Painter standing beside his artwork"></div>
    <figcaption class="cap">Maestro Ostiguín</figcaption>
  </figure>
  <figure class="photo" style="left:154px;top:112px;width:112px;height:100px">
    <div class="shot room" role="img" aria-label="Dining room with paintings on the walls"></div>
    <figcaption class="cap">Our dining room / artwork exposition</figcaption>
  </figure>
  <figure class="photo" style="left:10px;top:198px;width:70px;height:66px;transform:rotate(-5deg)">
    <div class="shot plate" role="img" aria-label="Plated stuffed cod"></div>
    <figcaption class="cap">Bacalao Relleno</figcaption>
  </figure>
  <figure class="photo" style="left:86px;top:194px;width:68px;height:68px;transform:rotate(4deg)">
    <div class="shot stew" role="img" aria-label="Bowl of osso buco"></div>
    <figcaption class="cap">Osso Buco</figcaption>
  </figure>
  <figure class="photo" style="left:152px;top:240px;width:110px;height:72px;transform:rotate(4deg)">
    <div class="shot mapfill" role="img" aria-label="Street map showing the restaurant location"></div>
    <figcaption class="cap">Our location on the map</figcaption>
  </figure>
  <figure class="photo" style="left:18px;top:270px;width:116px;height:112px">
    <div class="shot crowd" role="img" aria-label="Guests enjoying an evening in the restaurant"></div>
    <figcaption class="cap">Great atmosphere, nice music and friendly</figcaption>
  </figure>

  <h1 class="welcome script">Welcome to</h1>
  <p class="brand">Casa Benvidal</p>

  <div class="card front-card">
    <p class="enjoy script">Enjoy our Menu!</p>
    <ul class="sections">
      <li>Soups &amp; Appetizers</li>
      <li>Meat &amp; Poultry Plates</li>
      <li>Fresh Fish &amp; Seafoods</li>
      <li>Risottos &amp; Vegetables</li>
      <li>House-made Desserts</li>
    </ul>
  </div>
</section>

<!-- Inner spread -->
<section class="spread spread-inner">
  <div class="fold" style="left:284px"></div>

  <div class="card page-card page-left">
    <h3 class="heading script" style="top:4px">Soups &amp; Appetizers</h3>
    <div class="col" style="left:12px;top:38px;width:104px">
      <div class="entry"><div class="item"><span>Appetizer Name</span><span class="dots"></span><span>$8</span></div><p class="ingr">ingredient1, ingredient2, ingredient3, etc.</p></div>
      <div class="entry"><div class="item"><span>Appetizer Name</span><span class="dots"></span><span>$12</span></div><p class="ingr">ingredient1, ingredient2, ingredient3, etc.</p></div>
      <div class="entry"><div class="item"><span>Appetizer Name</span><span class="dots"></span><span>$8</span></div><p class="ingr">ingredient1, ingredient2, ingredient3, etc.</p></div>
      <div class="entry"><div class="item"><span>Appetizer Name</span><span class="dots"></span><span>$12</span></div><p class="ingr">Traditional ingredient1, ingredient2, etc.</p></div>
      <div class="entry"><div class="item"><span>Appetizer Name</span><span class="dots"></span><span>$12</span></div><p class="ingr">Traditional ingredient1, ingredient2, etc.</p></div>
    </div>
    <div class="col" style="left:130px;top:38px;width:102px">
      <div class="entry"><div class="item"><span>Appetizer Name</span><span class="dots"></span><span>$12</span></div><p class="ingr">ingredient1, ingredient2, ingredient3, etc.</p></div>
      <div class="entry"><div class="item"><span>Appetizer Name</span><span class="dots"></span><span>$12</span></div><p class="ingr">ingredient1, ingredient2, ingredient3, etc.</p></div>
      <div class="entry"><div class="item"><span>Appetizer Name</span><span class="dots"></span><span>$8</span></div><p class="ingr">ingredient1, ingredient2, ingredient3, etc.</p></div>
      <div class="entry" style="width:58px"><div class="item"><span>Appetizer</span><span class="dots"></span><span>$8</span></div><p class="ingr">ingredient1, ingredient2</p></div>
      <div class="entry" style="width:58px"><div class="item"><span>Appetizer</span><span class="dots"></span><span>$8</span></div><p class="ingr">ingredient1, ingredient2</p></div>
      <div class="entry" style="width:58px"><div class="item"><span>Appetizer</span><span class="dots"></span><span>$8</span></div><p class="ingr">ingredient1, ingredient2</p></div>
    </div>

    <h3 class="heading script" style="top:152px">Meat &amp; Poultry Plates</h3>
    <div class="col" style="left:12px;top:186px;width:220px">
      <div class="entry"><div class="item"><span>Meat Plate Name</span><span class="dots"></span><span>$8</span></div><p class="ingr">ingredient1, ingredient2, ingredient3, ingredient4 etc.</p></div>
      <div class="entry"><div class="item"><span>Meat Plate Name</span><span class="dots"></span><span>$12</span></div><p class="ingr">ingredient1, ingredient2, ingredient3, ingredient4 etc.</p></div>
      <div class="entry"><div class="item"><span>Meat Plate Name</span><span class="dots"></span><span>$8</span></div><p class="ingr">Traditional ingredient1, ingredient2, ingredient3, ingredient4 etc.</p></div>
      <div class="entry"><div class="item"><span>Filete a las 4 pimientas</span><span class="dots"></span><span>$12</span></div><p class="ingr">ingredient1, ingredient2, ingredient3, ingredient4 etc.</p></div>
      <div class="entry"><div class="item"><span>Meat Plate Name</span><span class="dots"></span><span>$8</span></div><p class="ingr">Traditional ingredient1, ingredient2, ingredient3, ingredient4 etc.</p></div>
    </div>
    <div class="col" style="left:12px;top:288px;width:104px">
      <div class="entry"><div class="item"><span>Meat Plate Name</span><span class="dots"></span><span>$12</span></div><p class="ingr">Traditional ingredient1, ingredient2</p></div>
      <div class="entry"><div class="item"><span>Meat Plate Name</span><span class="dots"></span><span>$8</span></div><p class="ingr">ingredient1, ingredient2, etc.</p></div>
      <div class="entry"><div class="item"><span>Meat Plate Name</span><span class="dots"></span><span>$8</span></div><p class="ingr">ingredient1, ingredient2, etc.</p></div>
      <div class="entry"><div class="item"><span>Meat Plate Name</span><span class="dots"></span><span>$12</span></div><p class="ingr">Traditional ingredient1, etc.</p></div>
    </div>
  </div>

  <figure class="photo" style="left:216px;top:88px;width:66px;height:66px;transform:rotate(5deg)">
    <div class="shot warm" role="img" aria-label="Steak with pepper sauce"></div>
    <figcaption class="cap">Filete a las 4 pimientas</figcaption>
  </figure>
  <figure class="photo" style="left:148px;top:306px;width:62px;height:66px;transform:rotate(-4deg)">
    <div class="shot stew" role="img" aria-label="Octopus special on a plate"></div>
    <figcaption class="cap">Pulpo Especial</figcaption>
  </figure>
  <figure class="photo" style="left:220px;top:302px;width:60px;height:64px;transform:rotate(6deg)">
    <div class="shot warm" role="img" aria-label="Steak with pepper sauce"></div>
    <figcaption class="cap">Filete a las 4 pimientas</figcaption>
  </figure>

  <div class="card page-card page-right">
    <h3 class="heading script" style="top:4px">Fish &amp; Seafood</h3>
    <div class="col" style="left:12px;top:38px;width:104px">
      <div class="entry"><div class="item"><span>Plate Name</span><span class="dots"></span><span>$8</span></div><p class="ingr">ingredient1, ingredient2, ingredient3, etc.</p></div>
      <div class="entry"><div class="item"><span>Plate Name</span><span class="dots"></span><span>$12</span></div><p class="ingr">ingredient1, ingredient2, ingredient3, etc.</p></div>
      <div class="entry"><div class="item"><span>Plate Name</span><span class="dots"></span><span>$8</span></div><p class="ingr">ingredient1, ingredient2, ingredient3, etc.</p></div>
      <div class="entry"><div class="item"><span>Plate Name</span><span class="dots"></span><span>$12</span></div><p class="ingr">Traditional ingredient1, ingredient2, etc.</p></div>
      <div class="entry"><div class="item"><span>Plate Name</span><span class="dots"></span><span>$8</span></div><p class="ingr">ingredient1, ingredient2, ingredient3, etc.</p></div>
    </div>
    <div class="col" style="left:130px;top:38px;width:104px">
      <div class="entry"><div class="item"><span>Plate Name</span><span class="dots"></span><span>$8</span></div><p class="ingr">ingredient1, ingredient2, ingredient3, etc.</p></div>
      <div class="entry"><div class="item"><span>Plate Name</span><span class="dots"></span><span>$12</span></div><p class="ingr">Traditional ingredient1, ingredient2, etc.</p></div>
    </div>

    <h3 class="heading script" style="top:152px">Risottos &amp; Vegetables</h3>
    <div class="col" style="left:12px;top:186px;width:104px">
      <div class="entry"><div class="item"><span>Risotto Plate Name</span><span class="dots"></span><span>$8</span></div><p class="ingr">ingredient1, ingredient2, ingredient3, etc.</p></div>
      <div class="entry"><div class="item"><span>Risotto Plate Name</span><span class="dots"></span><span>$12</span></div><p class="ingr">ingredient1, ingredient2, ingredient3, etc.</p></div>
      <div class="entry"><div class="item"><span>Risotto Plate Name</span><span class="dots"></span><span>$8</span></div><p class="ingr">ingredient1, ingredient2, ingredient3, etc.</p></div>
      <div class="entry"><div class="item"><span>Vegetable Plate Name</span><span class="dots"></span><span>$12</span></div><p class="ingr">ingredient1, ingredient2, ingredient3, etc.</p></div>
    </div>
    <div class="col" style="left:130px;top:186px;width:104px">
      <div class="entry"><div class="item"><span>Vegetable Plate Name</span><span class="dots"></span><span>$8</span></div><p class="ingr">ingredient1, ingredient2, ingredient3, etc.</p></div>
      <div class="entry"><div class="item"><span>Vegetable Plate Name</span><span class="dots"></span><span>$12</span></div><p class="ingr">ingredient1, ingredient2, ingredient3, etc.</p></div>
      <div class="entry"><div class="item"><span>Vegetable Plate Name</span><span class="dots"></span><span>$8</span></div><p class="ingr">ingredient1, ingredient2, ingredient3, etc.</p></div>
      <div class="entry"><div class="item"><span>Vegetable Plate Name</span><span class="dots"></span><span>$12</span></div><p class="ingr">ingredient1, ingredient2, ingredient3, etc.</p></div>
    </div>

    <h3 class="heading script" style="top:274px">Drinks &amp; Desserts</h3>
    <div class="col" style="left:12px;top:308px;width:104px">
      <div class="entry"><div class="item"><span>Dessert Name</span><span class="dots"></span><span>$7</span></div><p class="ingr">ingredient1, ingredient2, ingredient3, etc.</p></div>
      <div class="entry"><div class="item"><span>Dessert Name</span><span class="dots"></span><span>$7</span></div><p class="ingr">ingredient1, ingredient2, ingredient3, etc.</p></div>
      <div class="entry"><div class="item"><span>Dessert Name</span><span class="dots"></span><span>$7</span></div><p class="ingr">ingredient1, ingredient2, ingredient3, etc.</p></div>
    </div>
    <div class="col drinks" style="left:130px;top:308px;width:104px">
      <div class="item"><span>Coffee Name</span><span class="dots"></span><span>$7</span></div>
      <div class="item"><span>Coffee Name</span><span class="dots"></span><span>$7</span></div>
      <div class="item"><span>Drink Name</span><span class="dots"></span><span>$7</span></div>
      <div class="item"><span>Drink Name</span><span class="dots"></span><span>$7</span></div>
      <div class="item"><span>Drink Name</span><span class="dots"></span><span>$7</span></div>
    </div>
  </div>

  <figure class="photo" style="left:432px;top:92px;width:64px;height:66px;transform:rotate(-4deg)">
    <div class="shot plate" role="img" aria-label="Plated stuffed cod"></div>
    <figcaption class="cap">Bacalao Relleno</figcaption>
  </figure>
  <figure class="photo" style="left:500px;top:88px;width:62px;height:66px;transform:rotate(5deg)">
    <div class="shot shrimp" role="img" aria-label="Grilled prawns"></div>
    <figcaption class="cap">Langostinos</figcaption>
  </figure>
</section>

</body>
</html>
```